Need Stunning, Visual Tree Identification Booklet

We are looking for a magazine/booklet style design for tree and plant identification. They need to be organized according to tree/plant type and contain a picture and tree/plant information. I would like to see 4 trees/plants per page. I will be including links for all the information needed but you will be responsible for gathering pictures as we have none to provide. This is not a booklet that will be sold or given out, it is solely to be used by our company internally for training and for presenting during sales meetings.

Target Market(s)

To be used by our sales staff when meeting with customers and selling trees and plants.

Industry/Entity Type

Landscape Gardening

Font styles to use
Serif

Requirements
Must have
• Attractive design that makes it easy to read and visual the trees and plants shown in the booklet. Design must be done in Adobe Illustrator or Adobe InDesign. Every tree/plant must have a picture, description, common name, Botanical name, Height, Width, Growth Rate, Function, Hardiness and Water Use. Would like to fit 4 trees/plants per page. Attached is a category outline.
Nice to have
• Clean, professional look. Using greens, whites and blacks

```html
<!DOCTYPE html>
<html lang="en">
<head>
<meta charset="UTF-8">
<title>Oakline Crew – Tree &amp; Plant Identification Cover</title>
<link href="https://fonts.googleapis.com/css2?family=Arvo:wght@700&family=Noto+Serif:wght@400&display=swap" rel="stylesheet">
<style>
  :root{
    --green:#2bb04a;
    --green-deep:#178a35;
    --green-soft:#8fd79f;
    --ink:#0b0b0b;
    --white:#ffffff;
    --stage:#d9d9d9;
  }
  *{margin:0;padding:0;box-sizing:border-box}
  html,body{width:1200px;height:1200px;overflow:hidden;background:var(--stage)}
  .canvas{position:relative;width:1200px;height:1200px}
  .cover{position:absolute;width:489px;height:633px;overflow:hidden}
  .cover--front{left:66px;top:91px;
    background:radial-gradient(ellipse 62% 52% at 50% 42%,var(--white) 0%,#e6f6ea 35%,var(--green-soft) 70%,var(--green) 100%)}
  .cover--back{left:637px;top:470px;background:var(--green)}
  .cover__bar{position:absolute;left:0;top:0;width:100%;height:50px;background:var(--ink)}
  .cover__shine{position:absolute;left:8%;top:53px;width:84%;height:9px;
    background:linear-gradient(90deg,transparent,var(--white) 30%,var(--white) 70%,transparent)}
  .brand{position:absolute;left:0;width:100%;display:flex;flex-direction:column;align-items:center;gap:10px}
  .cover--front .brand{top:84px}
  .brand__mark{width:96px;height:96px;border-radius:50%;border:4px solid var(--green-deep)}
  .brand__name{font-family:"Arvo",serif;font-weight:700;font-size:26px;color:var(--green-deep);letter-spacing:1px}
  .glow{position:absolute;left:119px;top:190px;width:256px;height:256px;border-radius:50%;
    background:radial-gradient(circle,var(--white) 0%,#e9f8ed 45%,rgba(255,255,255,0) 72%)}
  .cover--back .brand{top:258px}
  .title{position:absolute;left:0;top:300px;width:100%;text-align:center}
  .title__main{font-family:"Arvo",serif;font-weight:700;font-size:38px;color:var(--green);line-height:1;letter-spacing:.5px}
  .title__amp{font-family:"Noto Serif",serif;font-weight:400;font-size:26px;color:var(--green-deep);margin:0 4px}
  .title__sub{font-family:"Noto Serif",serif;font-size:16px;letter-spacing:9px;color:var(--ink);margin-top:6px;padding-left:30px}
  .photo-grid{position:absolute;left:27px;top:389px;display:grid;grid-template-columns:repeat(4,103px);grid-template-rows:repeat(2,74px);gap:8px 8px}
  .photo{border:2px solid #1d1d1d}
  .contact{position:absolute;left:0;width:100%;text-align:center}
  .cover--front .contact{top:560px}
  .cover--back .contact{top:564px}
  .contact__band{margin:0 auto;width:82%;height:32px;display:flex;align-items:center;justify-content:center;
    background:linear-gradient(90deg,transparent,var(--white) 20%,var(--white) 80%,transparent)}
  .contact__phone{font-family:"Noto Serif",serif;font-size:27px;color:var(--green);letter-spacing:1.5px}
  .contact__web{font-family:"Noto Serif",serif;font-size:11px;letter-spacing:5px;color:var(--ink);margin-top:6px}
</style>
</head>
<body>
<main class="canvas">
  <section class="cover cover--front">
    <div class="cover__bar"></div>
    <div class="cover__shine"></div>
    <div class="brand">
      <span class="brand__mark"></span>
      <span class="brand__name">Oakline Crew</span>
    </div>
    <div class="title">
      <div class="title__main">TREE<span class="title__amp">&amp;</span>PLANT</div>
      <div class="title__sub">IDENTIFICATION</div>
    </div>
    <div class="photo-grid">
      <div class="photo" role="img" aria-label="Palm trees beside a house" style="background:linear-gradient(#6b9fd6,#8fa86a 60%,#c9a58a)"></div>
      <div class="photo" role="img" aria-label="Young trees in a nursery yard" style="background:linear-gradient(#b9d2e8,#6f9a4c 55%,#b59a78)"></div>
      <div class="photo" role="img" aria-label="Oranges on a branch" style="background:radial-gradient(circle at 55% 55%,#f08a1c 30%,#3d5a25 75%)"></div>
      <div class="photo" role="img" aria-label="Lemon among leaves" style="background:radial-gradient(circle at 70% 55%,#d8c23a 20%,#3f6a2c 65%)"></div>
      <div class="photo" role="img" aria-label="Pink daisy-like flower" style="background:radial-gradient(circle,#f0c060 10%,#e0459a 35%,#3a4a22 80%)"></div>
      <div class="photo" role="img" aria-label="Yellow flowering shrub" style="background:radial-gradient(circle,#f2d21c 25%,#2f5a20 75%)"></div>
      <div class="photo" role="img" aria-label="Shrub with small purple flowers" style="background:linear-gradient(135deg,#4f8a3a,#8a86c6 50%,#3e6d2a)"></div>
      <div class="photo" role="img" aria-label="Variegated ground cover leaves" style="background:linear-gradient(135deg,#2e4a22,#9bb88a 50%,#2e4a22)"></div>
    </div>
    <div class="contact">
      <div class="contact__band"><span class="contact__phone">(000) 444-1234</span></div>
      <div class="contact__web">WWW.DOMAIN.COM</div>
    </div>
  </section>

  <section class="cover cover--back">
    <div class="cover__bar"></div>
    <div class="cover__shine"></div>
    <div class="glow"></div>
    <div class="brand">
      <span class="brand__mark"></span>
      <span class="brand__name">Oakline Crew</span>
    </div>
    <div class="contact">
      <div class="contact__band"><span class="contact__phone">(000) 444-1234</span></div>
      <div class="contact__web">WWW.DOMAIN.COM</div>
    </div>
  </section>
</main>
</body>
</html>
```